Energy cost saving website (job description rewritten!)

Job Type: WordPress design
Task Outline: Create a WordPress design
Task Description:
We are new business (Germany) in the market of saving costs by power-saving (name: 'wir-falten-eure-Wolkenbögen.de'). This is reached by changing the supplier, the use of LED bulbs, energy saving washing machines, stoves, microwaves, hairdryers, vacuum cleaners and the like - where all of these be selled or affiliated through the website maybe you will create for us.
Design parameters:
We want a serious design that embodies a feeling of honesty, competence and capability.
Visitors should particularly see that this site saves them money!
The home page mainly should act as a selector of possibilities saving money by power-saving, usage of LED bulbs and large energy saving household devices (washing machines, etc.)
Updates
Hello designers,
browsing through the PixelHarbors files of portfolios I found one header graphics which excites me. Please find it here: http://www.pixelharbor-example.net/design/482716/wordpress-design-by-tarek-olumide . Note: it is NOT the picture but the shadowing. So if you consider this in your concepts would be another 'nice-to-have'.
Thanks.
Target Market(s)
People looking out for saving money by power-saving.
Industry/Entity Type
Business
Requirements
Must have
- Look and feel of 'this site saves me money'!
Nice to have
- We love 3D effects, but its not a must have. We also like cartoons, but feel free to develop your own concept, please. An appropriate backgrond picture would be nice.
Should not have
- Some kind of these exaggerated smiling or handshaking photos. That bathetic symbols like money bills or coins stacks.

```html
<!DOCTYPE html>
<html lang="en">
<head>
<meta charset="utf-8">
<title>wir-falten-eure-Wolkenbögen.de</title>
<link href="https://fonts.googleapis.com/css2?family=Open+Sans:ital,wght@0,400;0,600;0,700;0,800;1,400&family=PT+Sans:wght@700&family=Noto+Serif:wght@400;700&family=Arvo:wght@400;700&display=swap" rel="stylesheet">
<style>
:root{
  --teal:#01708f;
  --teal-dark:#014f68;
  --teal-text:#146f87;
  --footer:#025d7a;
  --cyan:#35d3ee;
  --pill-top:#bff3fd;
  --pill-bottom:#34c6ea;
  --navy:#083a58;
  --grey-bg:#f1f1f1;
  --thumb-border:#c6c6c6;
  --text:#5a5a5a;
  --heading-grey:#6b6b6b;
  --orange:#ee5a2e;
  --white:#ffffff;
}
*{box-sizing:border-box;margin:0;padding:0}
html,body{width:945px;height:1200px;overflow:hidden;background:var(--white)}
body{position:relative;font-family:'Open Sans',sans-serif;color:var(--text)}
.abs{position:absolute}

/* header */
.site-header{left:0;top:0;width:945px;height:85px;background:linear-gradient(#ffffff,#e9e9e9);border-bottom:1px solid #d0d0d0}
.brand{left:112px;top:24px;font-family:'PT Sans',sans-serif;font-weight:700;font-size:24px;color:#111;letter-spacing:-0.3px}
.search{left:634px;top:31px;width:198px;height:21px;border:1px solid #c9c9c9;border-radius:2px;background:#fff;font-size:9px;color:#888;padding:4px 6px}
.search svg{position:absolute;right:3px;top:2px}

/* hero */
.hero{left:0;top:85px;width:945px;height:417px;background:radial-gradient(ellipse 60% 70% at 50% 45%,#0b86a8 0%,#01708f 55%,#01556f 100%);overflow:hidden}
.hero-title{left:0;width:755px;top:22px;text-align:center;font-family:'Open Sans',sans-serif;font-weight:800;font-size:31px;color:#fff;letter-spacing:0.5px}
.pill{width:130px;height:38px;border-radius:12px;background:linear-gradient(var(--pill-top),var(--pill-bottom));box-shadow:0 2px 3px rgba(0,0,0,.35);color:#0b4f77;font-size:12.5px;line-height:14px;text-align:center;display:flex;align-items:center;justify-content:center}
.pillar-photo{width:154px;height:154px;border-radius:50%;background:#fff;box-shadow:0 6px 10px rgba(0,0,0,.3);overflow:hidden}
.pillar-photo span{position:absolute;inset:14px;border-radius:50%}
.slogan{left:680px;width:165px;top:114px;text-align:center;font-family:'Arvo',serif;font-size:18px;line-height:22px;color:var(--cyan)}
.promise{left:680px;width:165px;top:328px;text-align:center;font-family:'Arvo',serif;font-weight:700;font-size:14.5px;line-height:19px;color:#fff}
.hero-dots{left:0;top:395px;width:945px;height:22px;background:rgba(0,30,50,.35)}

/* carousel */
.carousel{left:0;top:502px;width:945px;height:158px;background:var(--grey-bg)}
.thumb{top:21px;width:122px;height:122px;border:4px solid var(--thumb-border);background:#fff;padding:6px}
.thumb span{display:block;width:100%;height:100%}
.divider-dots{left:0;top:660px;width:945px;height:8px;background:repeating-linear-gradient(90deg,#c9c9c9 0 2px,#ececec 2px 4px)}

/* welcome */
.welcome-title{left:111px;top:706px;font-family:'Noto Serif',serif;font-size:24px;line-height:25px;color:var(--heading-grey);font-weight:700;letter-spacing:-0.3px}
.welcome-title b{display:block;color:var(--teal-text)}
.welcome-copy{left:111px;top:771px;width:478px;font-size:10.5px;line-height:16.5px;color:var(--text)}
.welcome-copy p{margin-bottom:16px}

/* enquiry */
.emergency{left:627px;top:680px;width:206px;height:112px}
.enquiry-title{left:627px;top:792px;font-family:'Noto Serif',serif;font-size:16px;color:var(--heading-grey)}
.enquiry-title em{font-style:normal;color:var(--orange)}
.field{left:627px;width:205px;height:25px;border:2px solid #e2e2e2;border-radius:5px;background:#fff;font-size:9.5px;font-style:italic;color:#9a9a9a;padding:4px 8px}
.submit{left:627px;top:955px;width:74px;height:25px;border-radius:4px;background:linear-gradient(#f86a3a,#e24d22);color:#fff;font-family:'Noto Serif',serif;font-size:14px;line-height:25px;padding-left:6px}

/* footer */
.site-footer{left:0;top:1022px;width:945px;height:178px;background:var(--footer)}
.footer-col{top:18px;width:190px;color:#fff}
.footer-col h3{font-family:'Noto Serif',serif;font-weight:400;font-size:14.5px;margin-bottom:9px}
.footer-col li{list-style:none;font-size:9.5px;line-height:16.3px}
.footer-col li::before{content:"→";font-size:8px;margin-right:5px;opacity:.85}
.footer-rule{left:111px;top:138px;width:720px;height:1px;background:rgba(255,255,255,.15)}
.copyright{left:111px;top:149px;font-size:9.5px;color:#fff}
.social{top:146px;width:20px;height:20px;border-radius:50%;background:#fff}
</style>
</head>
<body>

<header class="abs site-header">
  <div class="abs brand">wir-falten-eure-Wolkenbögen</div>
  <div class="abs search">Type Search here...
    <svg width="16" height="15" viewBox="0 0 16 15"><circle cx="6" cy="6" r="4.3" fill="none" stroke="#555" stroke-width="1.6"/><line x1="9.2" y1="9.2" x2="14" y2="13.5" stroke="#555" stroke-width="2.2"/></svg>
  </div>
</header>

<section class="abs hero">
  <h1 class="abs hero-title">MONEY SAVING PILLARS</h1>

  <svg class="abs" style="left:0;top:0" width="945" height="417" viewBox="0 0 945 417">
    <g stroke="#5fc0da" stroke-width="1" stroke-dasharray="2 2" opacity=".7">
      <line x1="186" y1="78" x2="186" y2="195"/>
      <line x1="376" y1="78" x2="376" y2="195"/>
      <line x1="567" y1="78" x2="567" y2="195"/>
    </g>
    <g fill="var(--navy)">
      <polygon points="266,258 280,258 280,250 292,268 280,286 280,278 266,278"/>
      <polygon points="456,258 470,258 470,250 482,268 470,286 470,278 456,278"/>
    </g>
    <path d="M643 248 C660 205 700 195 722 215" fill="none" stroke="var(--navy)" stroke-width="11" stroke-linecap="round"/>
    <polygon points="712,200 738,222 708,232" fill="var(--navy)"/>
  </svg>

  <div class="abs pill" style="left:124px;top:117px">Change Electricity<br>Provider</div>
  <div class="abs pill" style="left:315px;top:117px">LED Bulbs</div>
  <div class="abs pill" style="left:506px;top:117px">Household<br>Appliances</div>

  <div class="abs pillar-photo" style="left:110px;top:192px"><span role="img" aria-label="Wind turbines and solar panel" style="background:radial-gradient(circle,#e4f1d6,#b9d3e6)"></span></div>
  <div class="abs pillar-photo" style="left:301px;top:192px"><span role="img" aria-label="Old light bulb replaced by LED bulbs" style="background:radial-gradient(circle,#f5f0d4,#dcdcdc)"></span></div>
  <div class="abs pillar-photo" style="left:491px;top:192px"><span role="img" aria-label="Blue washing machine" style="background:radial-gradient(circle,#6a7fd0,#2d3f99)"></span></div>

  <div class="abs slogan">SAVING MONEY<br>BY<br>POWER-SAVING</div>
  <div class="abs" role="img" aria-label="Piggy bank with banknotes" style="left:716px;top:192px;width:104px;height:122px;border-radius:50% 50% 45% 45%;background:radial-gradient(circle at 45% 55%,#fbc7dc,#ee8bb5)"></div>
  <div class="abs promise">WE LOWER YOUR<br>ELECTRICITY BILL</div>

  <div class="abs hero-dots">
    <svg class="abs" style="left:429px;top:3px" width="68" height="16" viewBox="0 0 68 16">
      <circle cx="8" cy="8" r="5.5" fill="#0b3f5a" stroke="#6fb3c8" stroke-width="1.2"/>
      <circle cx="25" cy="8" r="5.5" fill="#0b3f5a"/>
      <circle cx="42" cy="8" r="5.5" fill="#0b3f5a"/>
      <circle cx="59" cy="8" r="5.5" fill="#0b3f5a"/>
    </svg>
  </div>
</section>

<section class="abs carousel">
  <svg class="abs" style="left:110px;top:65px" width="18" height="34" viewBox="0 0 18 34"><polyline points="16,1 2,17 16,33" fill="none" stroke="#555" stroke-width="1.5"/></svg>
  <div class="abs thumb" style="left:137px"><span role="img" aria-label="LED and energy saving bulbs" style="background:radial-gradient(circle,#f3f3f3,#cfd3d6)"></span></div>
  <div class="abs thumb" style="left:274px"><span role="img" aria-label="White washing machine" style="background:radial-gradient(circle,#fafafa,#dadada)"></span></div>
  <div class="abs thumb" style="left:411px"><span role="img" aria-label="Stainless steel stove" style="background:radial-gradient(circle,#cfcfcf,#8c8c8c)"></span></div>
  <div class="abs thumb" style="left:548px"><span role="img" aria-label="Vacuum cleaner" style="background:radial-gradient(circle,#d8d8d8,#f3d78a)"></span></div>
  <div class="abs thumb" style="left:685px"><span role="img" aria-label="Hairdryer" style="background:radial-gradient(circle,#f8f4e6,#e8c44a)"></span></div>
  <svg class="abs" style="left:816px;top:65px" width="18" height="34" viewBox="0 0 18 34"><polyline points="2,1 16,17 2,33" fill="none" stroke="#555" stroke-width="1.5"/></svg>
</section>
<div class="abs divider-dots"></div>

<main>
  <h2 class="abs welcome-title">Welcome To<b>Wir-falten-eure-Wolkenbögen</b></h2>
  <div class="abs welcome-copy">
    <p>Lorem Ipsum is simply dummy text of the printing and typesetting industry. Lorem Ipsum has been the industry's standard dummy text ever since the 1500s, when an unknown printer took a galley of type and scrambled it to make a type specimen book.</p>
    <p>It has survived not only five centuries, but also the leap into electronic typesetting, remaining essentially unchanged.</p>
    <p>It was popularised in the 1960s with the release of Markwell sheets containing Lorem Ipsum passages, and more recently with desktop publishing software like Quillset Layout including versions of Lorem Ipsum.</p>
  </div>

  <aside>
    <svg class="abs emergency" viewBox="0 0 206 112">
      <defs>
        <linearGradient id="band" x1="0" y1="0" x2="0" y2="1"><stop offset="0" stop-color="#ffe600"/><stop offset="1" stop-color="#f08a00"/></linearGradient>
        <linearGradient id="plate" x1="0" y1="0" x2="0" y2="1"><stop offset="0" stop-color="#e3e3e3"/><stop offset="1" stop-color="#ffffff"/></linearGradient>
      </defs>
      <rect x="0" y="42" width="206" height="70" fill="url(#plate)"/>
      <polygon points="10,31 196,31 196,72 120,72 103,92 86,72 10,72" fill="url(#band)"/>
      <text x="103" y="30" text-anchor="middle" font-family="Open Sans, sans-serif" font-weight="800" font-size="34" fill="#5e5e5e" letter-spacing="-1">24 HOUR</text>
      <text x="103" y="54" text-anchor="middle" font-family="Open Sans, sans-serif" font-weight="700" font-size="15" fill="#fff">EMERGENCY</text>
      <text x="103" y="72" text-anchor="middle" font-family="Open Sans, sans-serif" font-weight="700" font-size="15" fill="#fff">SERVICE!</text>
    </svg>
    <h3 class="abs enquiry-title">Quick <em>Enquiry</em></h3>
    <div class="abs field" style="top:822px">Enter your name:</div>
    <div class="abs field" style="top:855px">Enter your email address:</div>
    <div class="abs field" style="top:888px">Enter your phone:</div>
    <div class="abs field" style="top:921px">Enter your location:</div>
    <div class="abs submit">Submit <span style="font-size:8px">▶</span></div>
  </aside>
</main>

<footer class="abs site-footer">
  <div class="abs footer-col" style="left:111px"><h3>Quick Links</h3><ul><li>Home</li><li>About Us</li><li>Services</li><li>Products</li><li>Contact Us</li></ul></div>
  <div class="abs footer-col" style="left:311px"><h3>Home Appliances</h3><ul><li>Washing Machines</li><li>Stoves</li><li>Microwaves</li><li>Hairdryers</li><li>Vacuum Cleaners</li></ul></div>
  <div class="abs footer-col" style="left:511px"><h3>Led Bulbs</h3><ul><li>Product 1</li><li>Product 2</li><li>Product 3</li><li>Product 4</li><li>Product 5</li></ul></div>
  <div class="abs footer-col" style="left:711px"><h3>Electricity Provider</h3><ul><li>Lorem Ipsum 1</li><li>Lorem Ipsum 2</li><li>Lorem Ipsum 3</li><li>Lorem Ipsum 4</li><li>Lorem Ipsum 5</li></ul></div>
  <div class="abs footer-rule"></div>
  <div class="abs copyright">©2012 wir-falten-eure-Wolkenbögen.de. All Rights Reserved.</div>
  <div class="abs social" style="left:761px" aria-label="Social link"></div>
  <div class="abs social" style="left:786px" aria-label="Social link"></div>
  <div class="abs social" style="left:811px" aria-label="Social link"></div>
</footer>

</body>
</html>
```